NCCS Brochure Design

Northbrook Council of Clinical Standards (NCCS) needs a whole new brochure. I've upload EPS logos and past brochures. Our tagline is to "modernize healthcare" and we think our brochure should reflect that, so that's the purpose of this project.

NCCS is a proven leader in healthcare education, training and
consulting services for health professionals. We’ve earned a reputation for excellence in healthcare quality improvement and management.

NCCS works to improve healthcare quality by educating healthcare professionals about healthcare best practices. We focus on instructing our clients on how to plan for, measure, and improve healthcare quality in all facilities and facets such as:

Patient Safety
Infection Control
Performance Improvement
Risk Management
Compliance and Accreditation
Health and Hospital Administration
Health Insurance
Healthcare Financial Management
Facility Management and Safety

DESIGN SUGGESTIONS:

Brochure Size: 8.5 X 11 full size brochure or 8.5 X 11 trifold brochure

Number of Pages: 2 to 3

Colors: Feel free to use a wide array of colors but try to stay away from colors that are too loud, ex: Pink, Purple, Neon Green.

Themes: Professional, Educational

Designs:

Korvel by Tobias Lindqvar

Palvex Leaflet by Derek Ostland

Gears for assembly by Quintoru

Figura de Sr KT by vrpq

http://www.plimsark.com/post/48210736651/10-creative-brochure-designs

Don't limit yourself to these examples. However, these are examples we liked
Updates

Project Deadline Extended
Reason: We would like to see more designs

We want more full page designs than tri-fold 

We are considering both tri-fold and full-page but would like to see more full page designs 

Project Deadline Extended

Project Deadline Extended
Reason: Our lead designer making the decisions on this project has been fired. I apologize for the inconvenience. We want extend the project one last time

Project Deadline Extended

Target Market(s)

Students, Doctors, and Educational Professionals

Industry/Entity Type

Healthcare

Logo Text

asdfasdf

Font styles to use
Serif
Sans Serif
Decorative
Script

Requirements
Should not have
• Pink, Purple, Neon Green colors

```html
<!DOCTYPE html>
<html lang="en">
<head>
<meta charset="utf-8">
<title>Northbrook Council of Clinical Standards – Back Cover</title>
<link rel="stylesheet" href="https://fonts.googleapis.com/css2?family=Arimo:wght@700&family=Crimson+Pro:wght@500;700&display=swap">
<style>
  :root {
    --paper: #ffffff;
    --navy: #1c2a6a;
    --label-grey: #8a8c8f;
    --icon-blue: #2f4c8c;
    --icon-teal: #1f7fb5;
    --icon-orange: #e0822a;
  }
  * { margin: 0; padding: 0; box-sizing: border-box; }
  html, body {
    width: 927px; height: 1200px; overflow: hidden; background: var(--paper);
  }
  .back-cover { position: relative; width: 927px; height: 1200px; overflow: hidden; }
  .backdrop { position: absolute; inset: 0; }
  .brand-name {
    position: absolute; left: 130px; top: 676px; width: 250px;
    font-family: "Crimson Pro", Georgia, serif; font-weight: 700;
    font-size: 22px; line-height: 25px; color: var(--navy);
  }
  .contact {
    position: absolute; left: 100px; top: 808px;
    display: grid; grid-template-columns: 86px auto;
    font-size: 16.5px; line-height: 22px;
  }
  .contact dt { font-family: "Arimo", Arial, sans-serif; font-weight: 700; color: var(--label-grey); }
  .contact dd { font-family: "Crimson Pro", Georgia, serif; font-weight: 500; color: var(--navy); }
  .social { position: absolute; left: 99px; top: 891px; display: flex; gap: 9px; list-style: none; }
  .social li { width: 37px; height: 37px; border-radius: 50%; box-shadow: 1px 2px 3px rgba(0,0,0,.35); }
  .social .channel-one { background: var(--icon-blue); }
  .social .channel-two { background: var(--icon-teal); }
  .social .channel-three { background: var(--icon-orange); }
</style>
</head>
<body>
<main class="back-cover">
  <svg class="backdrop" width="927" height="1200" viewBox="0 0 927 1200" aria-hidden="true">
    <defs>
      <radialGradient id="glow-upper" cx="580" cy="330" r="560" gradientUnits="userSpaceOnUse">
        <stop offset="0" stop-color="#ffffff"/>
        <stop offset="0.3" stop-color="#f9f9f9"/>
        <stop offset="0.75" stop-color="#e0e1e2"/>
        <stop offset="1" stop-color="#cfd0d2"/>
      </radialGradient>
      <radialGradient id="glow-lower-left" cx="270" cy="1040" r="330" gradientUnits="userSpaceOnUse">
        <stop offset="0" stop-color="#ffffff"/>
        <stop offset="0.5" stop-color="#eeeeef"/>
        <stop offset="1" stop-color="#d2d3d5"/>
      </radialGradient>
      <radialGradient id="glow-lower-right" cx="800" cy="1050" r="300" gradientUnits="userSpaceOnUse">
        <stop offset="0" stop-color="#ffffff"/>
        <stop offset="0.5" stop-color="#eeeeef"/>
        <stop offset="1" stop-color="#d2d3d5"/>
      </radialGradient>
    </defs>
    <rect class="panel-upper" x="0" y="0" width="927" height="757" fill="url(#glow-upper)"/>
    <polygon class="stripe-upper" points="927,152 927,314 701,757 621,757" fill="var(--paper)"/>
    <rect class="band-contact" x="0" y="757" width="927" height="187" fill="var(--paper)"/>
    <rect class="panel-lower" x="0" y="944" width="927" height="256" fill="url(#glow-lower-left)"/>
    <polygon class="panel-lower-right" points="606,944 927,944 927,1200 477,1200" fill="url(#glow-lower-right)"/>
    <polygon class="stripe-lower" points="523,944 606,944 477,1200 394,1200" fill="var(--paper)"/>
  </svg>

  <p class="brand-name">Northbrook Council of<br>Clinical Standards</p>

  <dl class="contact">
    <dt>Address:</dt><dd>2870 Harrow Ridge Avenue&nbsp; Northbrook, OK 73450</dd>
    <dt>Phone:</dt><dd>555-318-0462</dd>
    <dt>Website:</dt><dd>www.northbrook-ccs-demo.com</dd>
  </dl>

  <ul class="social" aria-label="Social channels">
    <li class="channel-one"></li>
    <li class="channel-two"></li>
    <li class="channel-three"></li>
  </ul>
</main>
</body>
</html>
```